Business Card Design Project

We consult with hotels on setting rates and maximizing a revenue strategy

Industry/Entity Type

Business

Contact Information for Business Card

I am not sure what I want. Our company offers high level consulting to hotels around the country but we are also laid back. I would like something that is professional but also shows the laid back side

```html
<!DOCTYPE html>
<html lang="en">
<head>
<meta charset="utf-8">
<title>Harborline Business Card</title>
<link rel="stylesheet" href="https://fonts.googleapis.com/css2?family=Ubuntu:wght@400;500&family=Roboto+Condensed:wght@300;400;700&display=swap">
<style>
  :root {
    --stage: #111111;
    --sky-top: #00b4ec;
    --sky-bottom: #f4f9fc;
    --teal: #1c6d66;
    --brown: #2e1c17;
    --ink: #3a3a3a;
    --rule: #6b6b6b;
    --paper: #ffffff;
  }
  * { margin: 0; padding: 0; box-sizing: border-box; }
  html, body {
    width: 1200px; height: 1200px; overflow: hidden;
    background: var(--stage);
  }
  .stage {
    width: 1200px; height: 1200px;
    display: flex; align-items: center; justify-content: center; gap: 40px;
  }
  .card {
    position: relative;
    width: 540px; height: 333px;
    overflow: hidden;
  }
  .card-front {
    background: linear-gradient(to top, var(--sky-bottom) 0%, #bfe6f7 45%, var(--sky-top) 100%);
  }
  .card-back { background: var(--paper); }

  .tab {
    position: absolute;
    top: 233px; width: 20px; height: 55px;
    background: var(--brown);
  }
  .card-front .tab { right: 0; }
  .card-back .tab { left: 0; }

  .web-address {
    position: absolute; top: 34px; right: 38px;
    font-family: "Ubuntu", sans-serif; font-size: 14px; color: var(--ink);
    letter-spacing: 0.2px;
  }
  .brand {
    position: absolute; left: 52px; top: 220px;
    display: flex; align-items: center; gap: 12px;
  }
  .brand-square {
    width: 22px; height: 22px; background: var(--teal);
  }
  .brand-name {
    font-family: "Roboto Condensed", sans-serif; font-weight: 700;
    font-size: 32px; color: var(--brown); letter-spacing: 0.5px;
  }
  .brand-tagline {
    position: absolute; left: 86px; top: 264px;
    font-family: "Roboto Condensed", sans-serif; font-weight: 400;
    font-size: 13px; color: var(--brown);
  }

  .person {
    position: absolute; left: 52px; top: 132px;
  }
  .person-name {
    font-family: "Ubuntu", sans-serif; font-weight: 400;
    font-size: 33px; color: var(--teal); line-height: 1;
  }
  .person-name strong { font-weight: 500; }
  .person-title {
    margin-top: 10px;
    font-family: "Ubuntu", sans-serif; font-size: 13px; color: var(--ink);
  }

  .contacts {
    position: absolute; right: 0; top: 128px;
    display: flex; flex-direction: column; align-items: flex-end;
  }
  .contact-line {
    font-family: "Roboto Condensed", sans-serif; font-weight: 300;
    font-size: 19px; color: var(--ink);
    padding: 0 42px 3px 0;
    border-bottom: 1px solid var(--rule);
    margin-bottom: 12px;
    text-align: right;
  }
  .contact-line .label { font-weight: 400; }
  .contact-office { width: 230px; }
  .contact-fax { width: 218px; }
  .contact-email { width: 264px; }
</style>
</head>
<body>
<main class="stage">
  <section class="card card-front" aria-label="Card front">
    <p class="web-address">www.HarborlineRMS.com</p>
    <div class="brand">
      <span class="brand-square"></span>
      <span class="brand-name">HARBORLINE</span>
    </div>
    <p class="brand-tagline">Revenue Management Solutions</p>
    <span class="tab"></span>
  </section>

  <section class="card card-back" aria-label="Card back">
    <span class="tab"></span>
    <div class="person">
      <p class="person-name"><strong>Dana</strong> Whitley</p>
      <p class="person-title">Regional Revenue Manager</p>
    </div>
    <div class="contacts">
      <p class="contact-line contact-office"><span class="label">Office</span> 555-014-0192</p>
      <p class="contact-line contact-fax"><span class="label">Fax</span> 555-014-0178</p>
      <p class="contact-line contact-email">Dana@HarborlineRMS.com</p>
    </div>
  </section>
</main>
</body>
</html>
```